Professional Business Card for Luxury Hotel & Resort Development Firm. Advisory firm

Project Overview: We are a specialized advisory firm focused on Hotel & Resort Development. Our clients are high-net-worth investors and major hospitality brands.

Design Requirements:

Style: Minimalist, sophisticated, and trustworthy. We want to avoid looking too "corporate" or "dry"—it should feel premium.

Key Elements: Please incorporate our logo [もしロゴがあれば] and emphasize a clean layout with plenty of white space.

Color Palette: We prefer Grey and White or Black and White to evoke a sense of luxury and stability.

Typography: Professional garamond, or sans-serif or elegant serif fonts

Goal: The card should feel substantial and high-end when handed to a client, reflecting our expertise in multi-million dollar developments.
Updates

I am currently on a business trip for field research and have limited access to my desktop. Additionally, I have just provided detailed technical feedback to a designer and am waiting for their refined proposals. To ensure the final logo meets the high standards of my new advisory firm, I would like to extend the deadline by 7 days. Thank you for your support.

Target Market(s)

High-net-worth investors, luxury hospitality brands, and real estate developers.

Contact Information for Business Card

Firm Name: Harbor Crest Partners, My Name: Kenji Morisawa, Title: Founder, Address 5-8-4 Kitanomura Aoba Yokohama Japan 225-0143, email address: kmorisawa@harborcrestpx.example, Tel: +81 90-4183-2750. Front Site (Primary): Japanese translation of the back side, Please use a clean Japanese font (like Mincho) that complements the Garmond on the English side Back side: English. Note for Japanese text: since the frond side is the main fae, please ensure the layout is clean and professional. Please use a high-quality Mincho ( Serif-style) font for Japanese to mach the Garmond used on the English side. Text for Front side (Japanese) Harbor Crest Partners, 役職:代表、森沢健二、225-0143 横浜市青葉区北野村5-8-4. Name of the firm can stay in English.

Font styles to use
Other font styles liked:
• Font Preference: Please use Garamond for all text to maintain a consistent, elegant, and classic professional look.

Requirements
Must have
• Professional and clean layout, high-end feel.
Nice to have
• Minimalist design with subtle luxury accents.

```html
<!DOCTYPE html>
<html lang="ja">
<head>
<meta charset="utf-8">
<title>Harbor Crest Partners — Business Card</title>
<link rel="stylesheet" href="https://fonts.googleapis.com/css2?family=EB+Garamond:wght@400;500;600;700&family=Noto+Serif+JP:wght@400;500&display=swap">
<style>
  :root {
    --backdrop: #9a9a9a;
    --card: #141414;
    --ink: #ffffff;
    --ink-soft: #ececec;
  }
  * { margin: 0; padding: 0; box-sizing: border-box; }
  html, body {
    width: 1200px;
    height: 1108px;
    overflow: hidden;
    background: var(--backdrop);
  }
  .canvas {
    position: relative;
    width: 1200px;
    height: 1108px;
  }
  .card {
    position: absolute;
    left: 242px;
    width: 716px;
    height: 409px;
    border-radius: 28px;
    background: var(--card);
    color: var(--ink);
  }
  .card--front { top: 119px; }
  .card--back { top: 581px; }

  .firm-name {
    position: absolute;
    left: 0;
    right: 0;
    text-align: center;
    font-family: "EB Garamond", Garamond, serif;
    font-weight: 600;
    letter-spacing: 0.5px;
    line-height: 1;
  }
  .card--front .firm-name { top: 40px; font-size: 46px; }
  .card--back .firm-name { top: 35px; font-size: 58px; }

  .jp {
    position: absolute;
    left: 0;
    right: 0;
    text-align: center;
    font-family: "Noto Serif JP", "EB Garamond", serif;
    font-weight: 400;
    line-height: 1;
  }
  .jp-title { top: 123px; font-size: 32px; }
  .jp-name { top: 178px; font-size: 46px; letter-spacing: 1px; }
  .jp-postal { top: 286px; font-size: 30px; font-family: "EB Garamond", "Noto Serif JP", serif; }
  .jp-postal .mark { font-family: "Noto Serif JP", serif; }
  .jp-address { top: 335px; font-size: 30px; }
  .jp-address .num { font-family: "EB Garamond", serif; }

  .identity {
    position: absolute;
    right: 383px;
    top: 183px;
    text-align: right;
    font-family: "EB Garamond", Garamond, serif;
    line-height: 1;
  }
  .identity .person { font-size: 31px; font-weight: 600; display: block; }
  .identity .role { font-size: 24px; font-weight: 400; display: block; margin-top: 10px; color: var(--ink-soft); }

  .divider {
    position: absolute;
    left: 352px;
    top: 196px;
    width: 2px;
    height: 62px;
    background: var(--ink);
  }

  .contact {
    position: absolute;
    left: 372px;
    list-style: none;
    font-family: "EB Garamond", Garamond, serif;
    font-size: 19px;
    color: var(--ink-soft);
  }
  .contact li {
    display: flex;
    align-items: center;
    height: 24px;
    margin-bottom: 11px;
  }
  .contact svg { width: 24px; height: 24px; margin-right: 8px; flex: none; }
  .contact { top: 198px; }

  .location {
    position: absolute;
    left: 0;
    right: 0;
    top: 351px;
    display: flex;
    justify-content: center;
    align-items: center;
    font-family: "EB Garamond", Garamond, serif;
    font-size: 17.5px;
    color: var(--ink-soft);
  }
  .location svg { width: 24px; height: 24px; margin-right: 10px; }
</style>
</head>
<body>
<main class="canvas">

  <section class="card card--front" lang="ja">
    <h1 class="firm-name" lang="en">Harbor Crest Partners</h1>
    <p class="jp jp-title">役職：代表</p>
    <p class="jp jp-name">森沢 健二</p>
    <p class="jp jp-postal"><span class="mark">〒</span>225-0143</p>
    <p class="jp jp-address">横浜市青葉区北野村<span class="num">5-8-4</span></p>
  </section>

  <section class="card card--back" lang="en">
    <h2 class="firm-name">Harbor Crest Partners</h2>

    <div class="identity">
      <span class="person">Kenji Morisawa</span>
      <span class="role">Founder</span>
    </div>

    <div class="divider"></div>

    <ul class="contact">
      <li>
        <svg viewBox="0 0 24 24" aria-hidden="true">
          <circle cx="12" cy="12" r="12" fill="#fff"/>
          <path d="M5.5 10.5c0-2 3-3.5 6.5-3.5s6.5 1.5 6.5 3.5l-2.3.6-.5-1.6c-1-.4-2.3-.6-3.7-.6s-2.7.2-3.7.6l-.5 1.6z" fill="#141414"/>
          <path d="M8.5 11h7l1.5 5.5H7z" fill="#141414"/>
          <circle cx="12" cy="13.8" r="1.4" fill="#fff"/>
        </svg>
        <span>+81 90-4183-2750</span>
      </li>
      <li>
        <svg viewBox="0 0 24 24" aria-hidden="true">
          <circle cx="12" cy="12" r="12" fill="#fff"/>
          <rect x="6" y="8" width="12" height="8.5" fill="none" stroke="#141414" stroke-width="1.4"/>
          <path d="M6 8l6 5 6-5M6 16.5l4.5-4.5M18 16.5l-4.5-4.5" fill="none" stroke="#141414" stroke-width="1.2"/>
        </svg>
        <span>kmorisawa@harborcrestpx.example</span>
      </li>
    </ul>

    <p class="location">
      <svg viewBox="0 0 24 24" aria-hidden="true">
        <circle cx="12" cy="12" r="12" fill="#fff"/>
        <path d="M12 4.5a5.2 5.2 0 0 0-5.2 5.2c0 3.8 5.2 9.3 5.2 9.3s5.2-5.5 5.2-9.3A5.2 5.2 0 0 0 12 4.5z" fill="#141414"/>
        <circle cx="12" cy="9.8" r="2" fill="#fff"/>
      </svg>
      <span>5-8-4 Kitanomura Aoba, Yokohama Japan 225-0143</span>
    </p>
  </section>

</main>
</body>
</html>
```